Travel Company Itinerary and Travel Packet

I run a travel company (agency) that organizes trips (any length i.e. day, week, month, or longer) to countries (Israel, Italy, Greece, etc). Regardless of the destination, we want to provide appealing, professional, and clean materials. We are a firm believer that our product is not just the trip but in everything we do...from our communication to our written/printed materials and online presence. Today we are specifically looking for a template that we can use to share one's trip/itinerary. Ideally what you would create would be a template we could populate with specific information for the client about the day-to-day of their trip, who we are, the hotels they are staying in, the highlights, what to pack, and where to eat, etc. To be more specific, this template should consist of the following:
1. Title Page (including contact info...however this could go where you see fit)
2. About Us (blurb about us at the company),
3. A highlights page of the trip and services included - this could be used as standalone marketing material for our clients to promote trips. (look at the Italy example)
4. A timeline of the process
5. A summary of the trip, bullet point/all one 1 page
6. A day-by-day itinerary page of what they are doing, and where they are staying (each day on its own page - should be the same template repeated for each day.
7. Recommended Hotels to choose from
8. Recommended Restaurants to eat at
9. A pricing page (per person, per group, itemized down to each experience.
10. A packing List
11. A letterhead that could be used for a cover letter
12. Each page should use pictures...a template where one could insert photos per page based on where the trip is going as well as stock imaging that brings the document to life for the reader. (see examples in uploaded files).

We've attached a few that we've seen in the industry that appeals to us and our tastes, but the template we are looking for is even more eye-popping, user-friendly, and communicates a high level of service just by seeing the document. It communicates our brand. Each attached example has elements we like and don't like and will give you. a good picture (we hope), but you'll notice the list we gave you provides a more robust end product...in other words we want more than these examples as we see great potential in including each layer of information with the ability to pick and choose what to include (from all of it to just the highlights page).

Link to Brand Assets- https://files.plovanexa.net/share/folders/8Kd24mTqZrw91XbLcVn3pYe60hJ?mode=view
Updates

We need a few days to review the designs and had a few requests for an extension if possible. I've also uploaded sample itineraries for Israel as requested by a few designers. Much appreciated

Target Market(s)

Any client of ours traveling - school, groups, families, big spenders etc

Industry/Entity Type

Travel Industry

Requirements
Must have
• See above list - if clarification is needed, I'm happy to give.

```html
<!DOCTYPE html>
<html lang="en">
<head>
<meta charset="utf-8">
<title>Solavanti Travel Packet Template</title>
<link href="https://fonts.googleapis.com/css2?family=Playfair+Display:wght@400;700&family=Montserrat:wght@400;600;700&display=swap" rel="stylesheet">
<style>
:root{
  --navy:#1f2b3b;
  --slate:#5e768a;
  --yellow:#e2da6b;
  --pale:#f1ec9c;
  --orange:#d98a40;
  --ink:#333a44;
  --grey:#8a8f96;
  --bg:#d5d5d5;
  --paper:#ffffff;
}
*{box-sizing:border-box}
html,body{margin:0;width:1200px;height:2356px;overflow:hidden;background:var(--bg)}
body{position:relative;font-family:'Montserrat',sans-serif;color:var(--ink)}
.page{position:absolute;width:300px;height:424px;background:var(--paper);overflow:hidden;box-shadow:3px 4px 8px rgba(0,0,0,.25)}
.topbar{position:absolute;top:0;left:0;right:0;height:12px;background:var(--navy)}
.topbar i{position:absolute;top:0;height:12px;width:9px;transform:skewX(-30deg)}
.topbar .s1{left:20px;background:var(--yellow)}
.topbar .s2{left:30px;background:var(--orange)}
.topbar .s3{left:40px;background:var(--pale)}
.band{position:absolute;left:4px;right:8px;top:34px;height:17px;margin:0;background:var(--yellow);font:400 14px/17px 'Playfair Display',serif;color:var(--navy);padding-left:18px}
.band::after{content:"";position:absolute;left:18px;right:12px;bottom:-3px;height:1px;background:var(--orange)}
.p{font:400 4.2px/1.5 'Montserrat',sans-serif;color:#4a4f57;margin:0}
.t{font:700 4.2px/1.4 'Montserrat',sans-serif;color:var(--navy);margin:0}
.abs{position:absolute}
.photo{position:absolute}
.foot{position:absolute;left:8px;right:0;bottom:0;height:40px}
.foot::before{content:"";position:absolute;left:0;right:10px;top:0;height:1px;background:var(--orange)}
.brand{position:absolute;left:4px;top:10px;display:flex;align-items:center;gap:3px;font:700 11px/1 'Montserrat',sans-serif;color:var(--navy)}
.brand b{width:9px;height:9px;border-radius:50%;background:var(--orange);display:block}
.contact{position:absolute;left:82px;top:13px;display:grid;grid-template-columns:58px 70px;row-gap:3px;font:600 3.6px/1 'Montserrat',sans-serif;color:var(--navy)}
.contact span::before{content:"";display:inline-block;width:3px;height:3px;border-radius:50%;background:var(--navy);margin-right:2px;vertical-align:middle}
.pn{position:absolute;right:-8px;bottom:4px;width:30px;height:26px;border-radius:50%;background:var(--yellow);font:600 4px/26px 'Montserrat',sans-serif;color:var(--navy);padding-left:10px}
.drop{display:block;width:16px;height:16px;background:var(--orange);border-radius:50% 0 50% 50%;transform:rotate(-45deg);flex:none}
.row{display:flex;gap:6px;align-items:flex-start}
ul.dot{list-style:none;margin:0;padding:0}
ul.dot li{font:400 3.8px/1.7 'Montserrat',sans-serif;color:#4a4f57;padding-left:5px;position:relative}
ul.dot li::before{content:"";position:absolute;left:0;top:1.6px;width:2px;height:2px;border:.5px solid var(--orange);border-radius:50%}
.tag{display:inline-block;background:var(--orange);color:#fff;font:600 5px/7px 'Montserrat',sans-serif;padding:0 4px;margin:1px 0 3px}
.serif{font-family:'Playfair Display',serif}
.cover-title{position:absolute;left:30px;top:30px;font:400 20px/1.05 'Playfair Display',serif;color:#fff;margin:0}
.cover-date{position:absolute;left:82px;top:72px;font:600 6px/1 'Montserrat',sans-serif;color:#fff}
.cover-place{position:absolute;left:20px;top:302px;font:700 19px/1 'Playfair Display',serif;color:#fff;margin:0}
.cover-sub{position:absolute;left:28px;top:322px;font:600 3.5px/1 'Montserrat',sans-serif;color:#fff}
.addr{font:400 3.4px/1.4 'Montserrat',sans-serif;color:var(--navy)}
.addr b{font-weight:700}
.sum{position:absolute;width:84px}
.sum .d{font:700 3.6px/1.5 'Montserrat',sans-serif;color:var(--navy)}
.daylbl{position:absolute;font:600 3.6px/1 'Montserrat',sans-serif;color:var(--orange)}
.hotel h4{margin:0;font:700 5px/1.3 'Montserrat',sans-serif;color:var(--navy)}
.hotel .room{font:400 5px/1.2 'Montserrat',sans-serif;color:var(--navy)}
.rest h4{margin:4px 0 3px;font:400 9px/1 'Playfair Display',serif;color:var(--orange)}
.rest .p{font-size:3.8px}
.pack h5{margin:0 0 3px;font:700 4.4px/1 'Montserrat',sans-serif;color:var(--orange);display:flex;justify-content:space-between}
.pack li{display:flex;justify-content:space-between}
</style>
</head>
<body>

<!-- Title page -->
<div class="page" style="left:455px;top:59px">
  <svg class="abs" style="left:0;top:0" width="300" height="424" viewBox="0 0 300 424">
    <defs>
      <linearGradient id="coverPhoto" x1="0" y1="0" x2="0" y2="1">
        <stop offset="0" stop-color="#9fb6c6"/>
        <stop offset=".3" stop-color="#b9ad95"/>
        <stop offset=".6" stop-color="#4e7a3f"/>
        <stop offset="1" stop-color="#6b9a4c"/>
      </linearGradient>
    </defs>
    <path role="img" aria-label="Aerial view of terraced gardens over a coastal city" d="M14 150 C20 80 80 40 160 40 C230 40 300 60 300 80 L300 310 C250 330 170 330 110 300 C50 270 10 220 14 150 Z" fill="url(#coverPhoto)"/>
    <path d="M0 0 H180 C205 40 185 100 120 112 C70 122 20 110 0 100 Z" fill="#5e768a" opacity=".95"/>
    <path d="M0 238 L112 316 L0 371 Z" fill="#d98a40"/>
  </svg>
  <h1 class="cover-title">LET'S GO<br>EXPERIENCE</h1>
  <div class="cover-date">JUNE 10th - 20th 2023</div>
  <h2 class="cover-place">Israel</h2>
  <div class="cover-sub">10 DAYS / 9 NIGHTS</div>
  <div class="brand" style="left:12px;top:385px;font-size:13px"><b></b>Solavanti</div>
  <div class="abs addr" style="left:120px;top:384px;width:90px"><b>USA</b><br>MN OFFICE - 210 Lakeview Court, Maple Bay, MN 55000<br>NY OFFICE - 88 Harbor Lane Suite 4B, NY 10000<br><b>1-800-555-0142</b></div>
  <div class="abs addr" style="left:225px;top:384px;width:70px"><b>ISRAEL</b><br>Olive Row 12, Ein Tamar, Israel 3800000<br><b>972-50-555-0187</b></div>
  <div class="abs addr" style="left:120px;top:413px">info@solavanti-travel.com &nbsp; www.solavanti-travel.com</div>
</div>

<!-- About us -->
<div class="page" style="left:134px;top:495px">
  <div class="topbar"><i class="s1"></i><i class="s2"></i><i class="s3"></i></div>
  <h2 class="band">About us</h2>
  <div class="abs" style="left:22px;top:60px;width:150px">
    <p class="p">Solavanti provides high-quality, experiential travel opportunities by developing relationships that uncover client desires and result in lasting memories created through shared connections to the land, people and history of a destination.</p>
    <p class="p" style="margin-top:5px">Let us take you on a journey where you explore, learn and experience the unexpected. Our engaging tours begin before you reach your destination - our team meets you virtually to learn your wants and needs, then creates the real-time moments that will leave an impact.</p>
  </div>
  <div class="photo" role="img" aria-label="Portrait of the team lead" style="left:209px;top:60px;width:46px;height:56px;background:#c9c9c9;border-radius:3px"></div>
  <div class="abs addr" style="left:210px;top:122px;line-height:1.8"><b>NAME OF PERSON</b><br>000-00-0000000<br>000-00-0000000<br><b>info@solavanti-travel.com</b></div>
  <div class="photo" role="img" aria-label="Travel team working together around a laptop" style="left:22px;top:208px;width:256px;height:146px;background:linear-gradient(135deg,#d9d3c9,#8f98a4 55%,#5d6672)"></div>
  <footer class="foot"><div class="brand"><b></b>Solavanti</div><div class="contact"><span>(USA) 1-800-555-0142</span><span>(ISRAEL) 972-50-555-0187</span><span>info@solavanti-travel.com</span><span>www.solavanti-travel.com</span></div><div class="pn">01</div></footer>
</div>

<!-- Trip & Services -->
<div class="page" style="left:452px;top:495px;background:var(--navy)">
  <div class="photo" role="img" aria-label="Tour coach on a desert road" style="left:110px;top:0;width:190px;height:95px;background:linear-gradient(90deg,rgba(31,43,59,1),rgba(140,120,95,.9) 60%,#b58d62)"></div>
  <div class="topbar" style="background:transparent"><i class="s1"></i><i class="s2"></i><i class="s3"></i></div>
  <h2 class="abs serif" style="left:20px;top:38px;margin:0;font-weight:400;font-size:14px;color:#fff">Trip &amp; Services</h2>
  <div class="abs" style="left:20px;top:56px;width:90px;height:1px;background:var(--orange)"></div>
  <p class="p abs" style="left:20px;top:60px;width:130px;color:#e5e8ec">Lorem Ipsum is simply dummy text of the printing and typesetting industry. Lorem Ipsum has been the industry's standard dummy text ever since the 1500s, when an unknown printer took a galley of type and scrambled it to make a type specimen book.</p>
  <div class="abs" style="left:20px;top:102px;width:260px;height:135px;background:#fff;padding:10px 12px">
    <div class="serif" style="font-size:8px;color:var(--navy);margin-bottom:8px">TRIP HIGHLIGHTS</div>
    <div style="display:grid;grid-template-columns:1fr 1fr;row-gap:9px;column-gap:10px">
      <div class="row"><i class="drop"></i><div><p class="t">LOREM IPSUM IS SIMPLY</p><p class="p" style="font-size:3.6px">Lorem Ipsum is simply dummy text of the printing and typesetting industry</p></div></div>
      <div class="row"><i class="drop"></i><div><p class="t">LOREM IPSUM IS SIMPLY</p><p class="p" style="font-size:3.6px">Lorem Ipsum is simply dummy text of the printing and typesetting industry</p></div></div>
      <div class="row"><i class="drop"></i><div><p class="t">LOREM IPSUM IS SIMPLY</p><p class="p" style="font-size:3.6px">Lorem Ipsum is simply dummy text of the printing and typesetting industry</p></div></div>
      <div class="row"><i class="drop"></i><div><p class="t">LOREM IPSUM IS SIMPLY</p><p class="p" style="font-size:3.6px">Lorem Ipsum is simply dummy text of the printing and typesetting industry</p></div></div>
      <div class="row"><i class="drop"></i><div><p class="t">LOREM IPSUM IS SIMPLY</p><p class="p" style="font-size:3.6px">Lorem Ipsum is simply dummy text of the printing and typesetting industry</p></div></div>
      <div class="row"><i class="drop"></i><div><p class="t">LOREM IPSUM IS SIMPLY</p><p class="p" style="font-size:3.6px">Lorem Ipsum is simply dummy text of the printing and typesetting industry</p></div></div>
      <div></div>
      <div class="row"><i class="drop"></i><div><p class="t">LOREM IPSUM IS SIMPLY</p><p class="p" style="font-size:3.6px">Lorem Ipsum is simply dummy text of the printing and typesetting industry</p></div></div>
    </div>
  </div>
  <div class="abs" style="left:20px;top:247px;width:280px;height:126px;background:var(--yellow);padding:9px 12px">
    <div class="serif" style="font-size:8px;color:var(--navy);margin-bottom:6px">SERVICES INCLUDED</div>
    <div style="display:grid;grid-template-columns:repeat(3,1fr);row-gap:6px;column-gap:6px">
      <div class="row" style="gap:3px"><i style="width:6px;height:6px;border-radius:50%;background:var(--orange);flex:none;margin-top:2px"></i><p class="p" style="font-size:3.4px">Lorem ipsum is simply dummy text of the printing</p></div>
      <div class="row" style="gap:3px"><i style="width:6px;height:6px;border-radius:50%;background:var(--orange);flex:none;margin-top:2px"></i><p class="p" style="font-size:3.4px">Lorem ipsum is simply dummy text of the printing</p></div>
      <div class="row" style="gap:3px"><i style="width:6px;height:6px;border-radius:50%;background:var(--orange);flex:none;margin-top:2px"></i><p class="p" style="font-size:3.4px">Lorem ipsum is simply dummy text of the printing</p></div>
      <div class="row" style="gap:3px"><i style="width:6px;height:6px;border-radius:50%;background:var(--orange);flex:none;margin-top:2px"></i><p class="p" style="font-size:3.4px">Lorem ipsum is simply dummy text of the printing</p></div>
      <div class="row" style="gap:3px"><i style="width:6px;height:6px;border-radius:50%;background:var(--orange);flex:none;margin-top:2px"></i><p class="p" style="font-size:3.4px">Lorem ipsum is simply dummy text of the printing</p></div>
      <div class="row" style="gap:3px"><i style="width:6px;height:6px;border-radius:50%;background:var(--orange);flex:none;margin-top:2px"></i><p class="p" style="font-size:3.4px">Lorem ipsum is simply dummy text of the printing</p></div>
      <div class="row" style="gap:3px"><i style="width:6px;height:6px;border-radius:50%;background:var(--orange);flex:none;margin-top:2px"></i><p class="p" style="font-size:3.4px">Lorem ipsum is simply dummy text of the printing</p></div>
      <div class="row" style="gap:3px"><i style="width:6px;height:6px;border-radius:50%;background:var(--orange);flex:none;margin-top:2px"></i><p class="p" style="font-size:3.4px">Lorem ipsum is simply dummy text of the printing</p></div>
      <div class="row" style="gap:3px"><i style="width:6px;height:6px;border-radius:50%;background:var(--orange);flex:none;margin-top:2px"></i><p class="p" style="font-size:3.4px">Lorem ipsum is simply dummy text of the printing</p></div>
      <div class="row" style="gap:3px"><i style="width:6px;height:6px;border-radius:50%;background:var(--orange);flex:none;margin-top:2px"></i><p class="p" style="font-size:3.4px">Lorem ipsum is simply dummy text of the printing</p></div>
      <div class="row" style="gap:3px"><i style="width:6px;height:6px;border-radius:50%;background:var(--orange);flex:none;margin-top:2px"></i><p class="p" style="font-size:3.4px">Lorem ipsum is simply dummy text of the printing</p></div>
      <div class="row" style="gap:3px"><i style="width:6px;height:6px;border-radius:50%;background:var(--orange);flex:none;margin-top:2px"></i><p class="p" style="font-size:3.4px">Lorem ipsum is simply dummy text of the printing</p></div>
    </div>
  </div>
  <footer class="foot" style="left:0;background:#fff;padding-left:8px"><div class="brand" style="left:12px"><b></b>Solavanti</div><div class="contact" style="left:90px"><span>(USA) 1-800-555-0142</span><span>(ISRAEL) 972-50-555-0187</span><span>info@solavanti-travel.com</span><span>www.solavanti-travel.com</span></div><div class="pn">02</div></footer>
</div>

<!-- Planning timeline -->
<div class="page" style="left:766px;top:495px">
  <div class="topbar"><i class="s1"></i><i class="s2"></i><i class="s3"></i></div>
  <h2 class="band">Planning Timeline</h2>
  <p class="p abs" style="left:22px;top:61px;width:250px">Lorem Ipsum is simply dummy text of the printing and typesetting industry. Lorem Ipsum has been the industry's standard dummy text ever since the 1500s, when an unknown printer took a galley of type and scrambled it to make a type specimen book.</p>
  <svg class="abs" style="left:0;top:0" width="300" height="424" viewBox="0 0 300 424">
    <g fill="none" stroke="#d98a40" stroke-width="5">
      <path d="M176 117 C150 117 130 150 130 169"/>
      <path d="M130 213 C130 230 150 245 158 245"/>
      <path d="M178 267 C178 280 160 294 152 294"/>
    </g>
    <g fill="#fff" stroke="#d98a40" stroke-width="5">
      <circle cx="176" cy="139" r="21"/><circle cx="130" cy="191" r="21"/>
      <circle cx="178" cy="245" r="21"/><circle cx="130" cy="294" r="21"/>
    </g>
    <g fill="none" stroke="#1f2b3b" stroke-width="1.6">
      <circle cx="172" cy="135" r="3"/><circle cx="181" cy="142" r="3"/><path d="M174 138 L179 140"/>
    </g>
    <circle cx="130" cy="190" r="6" fill="#1f2b3b"/><path d="M127 190 l2 2 l4 -4" stroke="#fff" stroke-width="1.3" fill="none"/>
    <path d="M168 247 L188 241 L190 243 L180 248 L172 252 Z" fill="#1f2b3b"/>
    <circle cx="130" cy="291" r="4" fill="#1f2b3b"/><path d="M122 301 q8 -8 16 0 z" fill="#1f2b3b"/>
    <g font-family="Montserrat,sans-serif" font-weight="700" font-size="26" fill="#d98a40">
      <text x="140" y="150">1</text><text x="148" y="203">2</text><text x="144" y="257">3</text><text x="148" y="306">4</text>
    </g>
  </svg>
  <div class="abs" style="left:210px;top:110px;width:70px"><div class="serif" style="font-size:5.5px;color:var(--navy)">TRIP DESIGN</div><p class="p" style="font-size:3.6px">Lorem ipsum is simply dummy text of the printing and typesetting industry. Lorem Ipsum has been the industry's standard dummy text ever since the 1500s, when an unknown printer took a galley of type.</p></div>
  <div class="abs" style="left:28px;top:162px;width:70px"><div class="serif" style="font-size:5.5px;color:var(--navy)">TRIP BOOKING<br>CONFIRMATION</div><p class="p" style="font-size:3.6px">Lorem ipsum is simply dummy text of the printing and typesetting industry. Lorem Ipsum has been the industry's standard dummy text ever since the 1500s.</p></div>
  <div class="abs" style="left:210px;top:220px;width:70px"><div class="serif" style="font-size:5.5px;color:var(--navy)">AFTER BOOKING<br>BEFORE DEPARTURE</div><p class="p" style="font-size:3.6px">Lorem ipsum is simply dummy text of the printing and typesetting industry. Lorem Ipsum has been the industry's standard dummy text ever since the 1500s.</p></div>
  <div class="abs" style="left:28px;top:283px;width:70px"><div class="serif" style="font-size:5.5px;color:var(--navy)">CUSTOMER SERVICE<br>&amp; ASSISTANCE DURING<br>YOUR TRIP</div><p class="p" style="font-size:3.6px">Lorem ipsum is simply dummy text of the printing and typesetting industry. Lorem Ipsum has been the industry's standard dummy text ever since the 1500s.</p></div>
  <footer class="foot"><div class="brand"><b></b>Solavanti</div><div class="contact"><span>(USA) 1-800-555-0142</span><span>(ISRAEL) 972-50-555-0187</span><span>info@solavanti-travel.com</span><span>www.solavanti-travel.com</span></div><div class="pn">03</div></footer>
</div>

<!-- Summary of the trip -->
<div class="page" style="left:134px;top:935px">
  <div class="topbar"><i class="s1"></i><i class="s2"></i><i class="s3"></i></div>
  <h2 class="band">Summary of The Trip</h2>
  <p class="p abs" style="left:24px;top:58px;width:250px">Lorem Ipsum is simply dummy text of the printing and typesetting industry. Lorem Ipsum has been the industry's standard dummy text ever since the 1500s, when an unknown printer took a galley of type and scrambled it to make a type specimen book.</p>
  <div class="abs" style="left:144px;top:84px;width:1px;height:290px;background:var(--orange)"></div>
  <div class="photo" role="img" aria-label="Ancient stone arch" style="left:107px;top:88px;width:36px;height:26px;background:linear-gradient(135deg,#c9b89a,#6e6455);border-radius:50% 0 50% 50%"></div>
  <svg class="abs" style="left:0;top:0" width="300" height="424" viewBox="0 0 300 424">
    <g fill="#d98a40">
      <path d="M142 156 h-18 a18 18 0 1 1 18 -18 z"/>
      <path d="M142 194 h-18 a18 18 0 1 1 18 -18 z"/>
      <path d="M142 232 h-18 a18 18 0 1 1 18 -18 z"/>
      <path d="M142 270 h-18 a18 18 0 1 1 18 -18 z"/>
      <path d="M142 308 h-18 a18 18 0 1 1 18 -18 z"/>
      <path d="M142 346 h-18 a18 18 0 1 1 18 -18 z"/>
      <path d="M147 136 h18 a18 18 0 1 0 -18 -18 z"/>
      <path d="M147 174 h18 a18 18 0 1 0 -18 -18 z"/>
      <path d="M147 212 h18 a18 18 0 1 0 -18 -18 z"/>
      <path d="M147 250 h18 a18 18 0 1 0 -18 -18 z"/>
      <path d="M147 288 h18 a18 18 0 1 0 -18 -18 z"/>
      <path d="M147 326 h18 a18 18 0 1 0 -18 -18 z"/>
      <path d="M147 364 h18 a18 18 0 1 0 -18 -18 z"/>
    </g>
  </svg>
  <div class="daylbl" style="left:113px;top:83px">DAY 1</div><div class="daylbl" style="left:168px;top:94px">DAY 2</div>
  <div class="daylbl" style="left:113px;top:121px">DAY 3</div><div class="daylbl" style="left:168px;top:132px">DAY 4</div>
  <div class="daylbl" style="left:113px;top:159px">DAY 5</div><div class="daylbl" style="left:168px;top:170px">DAY 6</div>
  <div class="daylbl" style="left:113px;top:197px">DAY 7</div><div class="daylbl" style="left:168px;top:208px">DAY 8</div>
  <div class="daylbl" style="left:113px;top:235px">DAY 9</div><div class="daylbl" style="left:168px;top:246px">DAY 10</div>
  <div class="daylbl" style="left:113px;top:273px">DAY 11</div><div class="daylbl" style="left:168px;top:284px">DAY 12</div>
  <div class="daylbl" style="left:113px;top:311px">DAY 12</div><div class="daylbl" style="left:168px;top:322px">DAY 14</div>
  <div class="sum" style="left:33px;top:92px"><div class="d">Friday June 10, 2023</div><div class="t">ARRIVAL + INTO THE DESERT</div><p class="p" style="font-size:3.4px">LUNCH - On your own<br>DINNER - Shabbat dinner at hotel</p></div>
  <div class="sum" style="left:33px;top:130px"><div class="d">Sunday June 12, 2023</div><div class="t">MORE MAGIC OF THE DESERT</div><p class="p" style="font-size:3.4px">LUNCH - On your own<br>DINNER - On your own</p></div>
  <div class="sum" style="left:33px;top:168px"><div class="d">Tuesday June 14, 2023</div><div class="t">TEL AVIV &amp; JAFFA FROM OLD TO NEW, MARKETS, ART &amp; CULTURE</div><p class="p" style="font-size:3.4px">LUNCH - On your own<br>DINNER - On your own</p></div>
  <div class="sum" style="left:33px;top:206px"><div class="d">Thursday June 16, 2023</div><div class="t">INTO THE DESERT, MASADA AND THE DEAD SEA</div><p class="p" style="font-size:3.4px">LUNCH - On your own<br>DINNER - On your own</p></div>
  <div class="sum" style="left:33px;top:246px"><div class="d">Saturday June 18, 2023</div><div class="t">SHABBAT IN JERUSALEM</div><p class="p" style="font-size:3.4px">LUNCH - On your own<br>DINNER - On your own</p></div>
  <div class="sum" style="left:33px;top:284px"><div class="d">Monday June 20, 2023</div><div class="t">FAREWELL TO ISRAEL</div><p class="p" style="font-size:3.4px">LUNCH - On your own<br>DINNER - On your own</p></div>
  <div class="sum" style="left:33px;top:322px"><div class="d">Saturday June 18, 2023</div><div class="t">LOREM IPSUM IS</div><p class="p" style="font-size:3.4px">LUNCH - On your own<br>DINNER - On your own</p></div>
  <div class="sum" style="left:196px;top:100px"><div class="d">Saturday June 11, 2023</div><div class="t">SHABBAT IN THE DESERT</div><p class="p" style="font-size:3.4px">LUNCH - Shabbat lunch<br>DINNER - On your own</p></div>
  <div class="sum" style="left:196px;top:138px"><div class="d">Monday June 13, 2023</div><div class="t">DIGGING INTO THE PAST &amp; A VISIT TO THE PARTNERSHIP REGION</div><p class="p" style="font-size:3.4px">LUNCH - On your own<br>DINNER - On your own</p></div>
  <div class="sum" style="left:196px;top:178px"><div class="d">Wednesday June 15, 2023</div><div class="t">BRIDGING THE GENERATIONS OF THE PAST &amp; PRESENT, ARRIVAL IN JERUSALEM</div><p class="p" style="font-size:3.4px">LUNCH - On your own<br>DINNER - On your own</p></div>
  <div class="sum" style="left:196px;top:218px"><div class="d">Friday June 17, 2023</div><div class="t">JERUSALEM THE ANCIENT</div><p class="p" style="font-size:3.4px">LUNCH - On your own<br>DINNER - On your own</p></div>
  <div class="sum" style="left:196px;top:256px"><div class="d">Sunday June 19, 2023</div><div class="t">MEMORY AND JERUSALEM THE NEW</div><p class="p" style="font-size:3.4px">LUNCH - On your own<br>DINNER - On your own</p></div>
  <div class="sum" style="left:196px;top:294px"><div class="d">Sunday June 19, 2023</div><div class="t">LOREM IPSUM IS</div><p class="p" style="font-size:3.4px">LUNCH - On your own<br>DINNER - On your own</p></div>
  <div class="sum" style="left:196px;top:332px"><div class="d">Sunday June 19, 2023</div><div class="t">LOREM IPSUM IS</div><p class="p" style="font-size:3.4px">LUNCH - On your own<br>DINNER - On your own</p></div>
  <footer class="foot"><div class="brand"><b></b>Solavanti</div><div class="contact"><span>(USA) 1-800-555-0142</span><span>(ISRAEL) 972-50-555-0187</span><span>info@solavanti-travel.com</span><span>www.solavanti-travel.com</span></div><div class="pn">04</div></footer>
</div>

<!-- Day itinerary -->
<div class="page" style="left:452px;top:935px">
  <div class="topbar"><i class="s1"></i><i class="s2"></i><i class="s3"></i></div>
  <div class="abs" style="left:150px;top:20px;height:14px;background:var(--navy);color:#fff;font:600 7px/14px 'Montserrat',sans-serif;padding:0 6px"><span style="text-decoration:underline;font-size:9px">DAY 1</span> &nbsp;<span style="color:var(--yellow)">FRIDAY JUNE 10, 2023</span></div>
  <h2 class="band" style="font-size:13px;padding-left:14px">ARRIVAL + INTO THE DESERT</h2>
  <div class="abs" style="left:32px;top:78px;width:240px">
    <div class="t" style="font-size:5px;text-decoration:underline;margin-bottom:4px">ITINERARY</div>
    <div class="t" style="font-size:3.8px;margin-bottom:3px">DAY 1 - ON THE WAY SOUTH</div>
    <ul class="dot">
      <li><b>Breakfast at the hotel</b></li>
      <li>The Garden Trail - We'll walk through the trail, a working farm and interactive museum designed to teach visitors what it takes to farm and grow crops in the desert.</li>
      <li><b>Lunch at the Garden Trail</b></li>
      <li><b>Sandboarding</b> - Slide down the stunning dunes, where anyone can be a surfer</li>
      <li>Check in to hotel and get ready for Shabbat</li>
      <li>Shabbat Service at the hotel and lighting candles</li>
      <li>Shabbat Dinner at the hotel</li>
    </ul>
    <p class="p" style="margin-top:6px;font-size:3.8px"><b>Overnight:</b> Desert Ridge Hotel, Ramon</p>
  </div>
  <div class="photo" role="img" aria-label="Fresh vegetable platter" style="left:14px;top:212px;width:108px;height:90px;background:radial-gradient(circle at 45% 45%,#f1e6d8,#9cae6b 50%,#c96a4a);border-radius:50% 0 50% 50%;transform:rotate(-15deg);border:3px solid var(--orange)"></div>
  <div class="photo" role="img" aria-label="Group hiking through a desert canyon pool" style="left:120px;top:192px;width:180px;height:118px;background:linear-gradient(180deg,#c2b8a8,#8c7d66 55%,#5d5a4c)"></div>
  <div class="abs" style="left:32px;top:320px;width:240px">
    <div class="t" style="font-size:5px;text-decoration:underline;margin-bottom:3px">SERVICES INCLUDED:</div>
    <ul class="dot">
      <li>Meals as detailed below</li>
      <li>9 nights at 4-5 star hotels. Accommodations are based on double occupancy</li>
      <li>1 professionally licensed guide educator with group on 24/7 basis (all accommodation and tour expenses included)</li>
      <li>1 deluxe motor coach with air conditioning daily and a refrigerator with cold water for the group on the road</li>
      <li>2 complimentary upgrades for organization staff, per availability</li>
      <li>Entrance fees and activity costs according to sample itinerary</li>
      <li>Gratuities for guide, driver and local guide</li>
    </ul>
  </div>
  <footer class="foot"><div class="brand"><b></b>Solavanti</div><div class="contact"><span>(USA) 1-800-555-0142</span><span>(ISRAEL) 972-50-555-0187</span><span>info@solavanti-travel.com</span><span>www.solavanti-travel.com</span></div><div class="pn">05</div></footer>
</div>

<!-- Hotels -->
<div class="page" style="left:766px;top:935px">
  <div class="topbar"><i class="s1"></i><i class="s2"></i><i class="s3"></i></div>
  <h2 class="band">Selection of Hotels</h2>
  <div class="abs hotel" style="left:40px;top:63px;width:102px"><h4>PALAZZO AURELIO</h4><div class="room">(Superior Room)</div><div class="tag">VENICE – 3 nights</div><p class="p" style="font-size:3.2px">With contemporary interior design, a wellness center and the most modern services, the hotel proposes a new hospitality concept in the historic heart of the city, close to the main square and the bridges.</p>
    <div class="photo" role="img" aria-label="Hotel bedroom with blue headboard" style="position:relative;margin-top:6px;width:102px;height:66px;background:linear-gradient(135deg,#2f4f7a,#8fa4bf 60%,#d9d6cf)"></div><p class="p" style="font-size:3px;margin-top:2px">www.palazzoaurelio.it</p></div>
  <div class="abs hotel" style="left:158px;top:63px;width:102px"><h4>VILLA FIORENZA</h4><div class="room">(Superior Room)</div><div class="tag">FLORENCE – 3 nights</div><p class="p" style="font-size:3.2px">The hotel features free Wi-Fi, a charming internal garden from the 19th century and a panoramic terrace with views of the city. It is a 10-minute walk from the old market.</p>
    <div class="photo" role="img" aria-label="Historic stone hotel facade" style="position:relative;margin-top:6px;width:102px;height:66px;background:linear-gradient(180deg,#a69887,#6f6253 60%,#8a8a86)"></div><p class="p" style="font-size:3px;margin-top:2px">www.villafiorenza.it</p></div>
  <div class="abs hotel" style="left:40px;top:210px;width:102px"><h4>HOTEL COSTA ALTA</h4><div class="room">(Comfort Room)</div><div class="tag">SORRENTO – 4 nights</div><p class="p" style="font-size:3.2px">Hotel Costa Alta is near the main square in the heart of town, featuring a citrus garden with a swimming pool. The helpful staff can help you plan day trips along the coast. Free Wi-Fi is available throughout.</p>
    <div class="photo" role="img" aria-label="Warm hotel lobby with patterned floor" style="position:relative;margin-top:6px;width:102px;height:66px;background:linear-gradient(135deg,#e2a04c,#b46a2c 55%,#f0d9a8)"></div><p class="p" style="font-size:3px;margin-top:2px">www.hotelcostaalta.com</p></div>
  <div class="abs hotel" style="left:158px;top:210px;width:102px"><h4>HOTEL COLONNA</h4><div class="room">(Superior Room)</div><div class="tag">ROMA – 4 nights</div><p class="p" style="font-size:3.2px">Hotel Colonna is a 4-star luxury hotel located in the center of the city, close to the main squares. The hotel is located in the building of an ancient theatre.</p>
    <div class="photo" role="img" aria-label="Rooftop terrace overlooking a domed church" style="position:relative;margin-top:6px;width:102px;height:66px;background:linear-gradient(180deg,#b9cbe0,#b8a890 60%,#6d6a68)"></div><p class="p" style="font-size:3px;margin-top:2px">www.hotelcolonna.com</p></div>
  <p class="p abs" style="left:20px;top:372px;width:260px;font-size:3px">Please note: all hotel stays will include full buffet breakfast and VAT taxes. Only city taxes need to be paid directly by the guest at checkout. City taxes currently range from 3 to 6 Euros per person per night.</p>
  <footer class="foot"><div class="brand"><b></b>Solavanti</div><div class="contact"><span>(USA) 1-800-555-0142</span><span>(ISRAEL) 972-50-555-0187</span><span>info@solavanti-travel.com</span><span>www.solavanti-travel.com</span></div><div class="pn">06</div></footer>
</div>

<!-- Restaurants -->
<div class="page" style="left:134px;top:1378px">
  <div class="topbar"><i class="s1"></i><i class="s2"></i><i class="s3"></i></div>
  <h2 class="band">Restaurants to Eat</h2>
  <div class="abs rest" style="left:40px;top:72px;width:100px"><div class="photo" role="img" aria-label="Dim restaurant interior with set tables" style="position:relative;width:100px;height:60px;background:linear-gradient(135deg,#2b2622,#6a5646 60%,#a08466)"></div><h4>NORTH</h4><p class="p">TYPE OF RESTAURANT - <b>Superior Room</b><br>PRICE - <b>$-$$$</b><br>TEAM MEMBER - <b>3 Nights</b><br>BEST MEAT MEAL - <b>Lorem Ipsum</b></p><p class="p" style="margin-top:2px;font-size:3.2px">Lorem ipsum is simply dummy text of the printing and typesetting industry. Lorem Ipsum has been the industry's standard dummy text.</p></div>
  <div class="abs rest" style="left:158px;top:72px;width:100px"><div class="photo" role="img" aria-label="Bright white dining room" style="position:relative;width:100px;height:60px;background:linear-gradient(135deg,#f4f1ea,#cfc7b8 60%,#a59a88)"></div><h4>SOUTH</h4><p class="p">TYPE OF RESTAURANT - <b>Superior Room</b><br>PRICE - <b>$-$$$</b><br>TEAM MEMBER - <b>2 Nights</b><br>BEST MEAT MEAL - <b>Lorem Ipsum</b></p><p class="p" style="margin-top:2px;font-size:3.2px">Lorem ipsum is simply dummy text of the printing and typesetting industry. Lorem Ipsum has been the industry's standard dummy text.</p></div>
  <div class="abs rest" style="left:40px;top:213px;width:100px"><div class="photo" role="img" aria-label="Candlelit dinner table" style="position:relative;width:100px;height:60px;background:linear-gradient(135deg,#1d1713,#5e3f2a 55%,#c48c54)"></div><h4>JERUSALEM</h4><p class="p">TYPE OF RESTAURANT - <b>Superior Room</b><br>PRICE - <b>$-$$$</b><br>TEAM MEMBER - <b>3 Nights</b><br>BEST MEAT MEAL - <b>Lorem Ipsum</b></p><p class="p" style="margin-top:2px;font-size:3.2px">Lorem ipsum is simply dummy text of the printing and typesetting industry. Lorem Ipsum has been the industry's standard dummy text.</p></div>
  <div class="abs rest" style="left:158px;top:213px;width:100px"><div class="photo" role="img" aria-label="Modern restaurant with blue lighting" style="position:relative;width:100px;height:60px;background:linear-gradient(135deg,#1e2a44,#3d5a86 55%,#9fb0c6)"></div><h4>TEL AVIV</h4><p class="p">TYPE OF RESTAURANT - <b>Superior Room</b><br>PRICE - <b>$-$$$</b><br>TEAM MEMBER - <b>3 Nights</b><br>BEST MEAT MEAL - <b>Lorem Ipsum</b></p><p class="p" style="margin-top:2px;font-size:3.2px">Lorem ipsum is simply dummy text of the printing and typesetting industry. Lorem Ipsum has been the industry's standard dummy text.</p></div>
  <p class="p abs" style="left:26px;top:362px;width:180px;font-size:3px">*Child 0-12 years of age sharing a room as a 3rd only<br>*Should the number of full-paying participants drop below 20, the agency reserves the right to amend costs<br>*Prices are dependent on the USD, therefore they may vary slightly</p>
  <footer class="foot"><div class="brand"><b></b>Solavanti</div><div class="contact"><span>(USA) 1-800-555-0142</span><span>(ISRAEL) 972-50-555-0187</span><span>info@solavanti-travel.com</span><span>www.solavanti-travel.com</span></div><div class="pn">07</div></footer>
</div>

<!-- Tour quotation -->
<div class="page" style="left:452px;top:1378px">
  <div class="topbar"><i class="s1"></i><i class="s2"></i><i class="s3"></i></div>
  <h2 class="band">Tour Quotation</h2>
  <div class="abs tag" style="left:26px;top:56px">TOUR PRICE</div>
  <div class="abs" style="left:26px;top:68px;width:250px;display:grid;grid-template-columns:70px 68px 1fr;font:600 4.8px/1.3 'Montserrat',sans-serif;color:var(--navy)">
    <div>*PER PERSON: for per group<br>15-20 people - $ 0.000<br>21-24 people - $ 0.000<br>25-29 people - $ 0.000</div>
    <div>*PER COUPLE:<br>30 people - $ 0.000</div>
    <div>*PER FAMILY:<br>4 PEOPLE<br>Transportation costs - $ 0.000<br>Guide Costs - $ 0.000<br>Driver Costs - $ 0.000<br>Grand Total - $ 0.000</div>
  </div>
  <div class="abs" style="left:26px;top:124px;width:248px;height:1px;background:var(--orange)"></div>
  <p class="p abs" style="left:26px;top:127px;width:180px;font-size:3.2px">*Based on 2 people traveling together and double occupancy, as indicated in the Accommodations Section<br>*Includes all services and accommodations mentioned in the program under Services Included<br>*This price does NOT include the international flight and all that is not mentioned under Services Included</p>
  <svg class="abs" style="left:28px;top:150px" width="16" height="18" viewBox="0 0 16 18"><path d="M8 1 L15 4 V9 C15 13 12 16 8 17 C4 16 1 13 1 9 V4 Z" fill="none" stroke="#d98a40" stroke-width="1.5"/><path d="M5 9 l2 2 l4 -4" fill="none" stroke="#d98a40" stroke-width="1.5"/></svg>
  <p class="t abs" style="left:50px;top:151px;width:200px;font-size:3.6px">We guarantee top quality of all the services included.<br>We guarantee full time assistance during your travel in Italy.<br>We will be happy to give you complimentary contacts of our selection of favorite local restaurants and book them for you if you wish.</p>
  <div class="abs" style="left:26px;top:178px;width:110px"><div class="t" style="font-size:4.2px;margin-bottom:2px">CONDITIONS</div><p class="p" style="font-size:3.2px">Prices are inclusive of all services mentioned in the program under services included. Prices are inclusive of VAT taxes and administrative fees. All service and hotels are subject to confirmation. Payment conditions: we require 30% non-refundable deposit to secure your booking.</p></div>
  <div class="abs" style="left:152px;top:178px;width:122px"><div class="t" style="font-size:4.2px;margin-bottom:2px">CANCELLATION POLICY</div><p class="p" style="font-size:3.2px">In case of cancellation of a confirmed tour, the following fees will be applied: from the day following the booking until 60 days prior to departure, deposit of your booking. Between 59 and 30 days prior to departure, 40% of tour price. From 29 days prior to departure, 100% of tour price.</p></div>
  <p class="t abs" style="left:26px;top:224px;font-size:4.4px">This offer is valid until: <span style="color:var(--orange)">November 27th 2023</span><br>and pending selected hotels' availability confirmation.</p>
  <div class="photo" role="img" aria-label="Couple with luggage checking a tablet at an airport" style="left:22px;top:246px;width:254px;height:110px;background:linear-gradient(135deg,#6b7f95,#b9a78a 50%,#e6d57a 75%,#3d6ea8)"></div>
  <footer class="foot"><div class="brand"><b></b>Solavanti</div><div class="contact"><span>(USA) 1-800-555-0142</span><span>(ISRAEL) 972-50-555-0187</span><span>info@solavanti-travel.com</span><span>www.solavanti-travel.com</span></div><div class="pn">08</div></footer>
</div>

<!-- Packing list -->
<div class="page" style="left:766px;top:1378px">
  <div class="topbar"><i class="s1"></i><i class="s2"></i><i class="s3"></i></div>
  <h2 class="band">Packing List</h2>
  <div class="abs pack" style="left:20px;top:62px;width:74px"><h5><span>TOILETRIES</span><span>QTY.</span></h5>
    <ul class="dot"><li><span>Shampoo &amp; Conditioner</span><span>2</span></li><li><span>Face Wash &amp; Moisturizer</span><span>2</span></li><li><span>Body Wash</span><span>1</span></li><li><span>Lotion</span><span>6</span></li><li><span>Razor</span><span>8</span></li><li><span>Deodorant</span><span>3</span></li><li><span>Cotton Balls &amp; Q-Tips</span><span>2</span></li><li><span>Toothbrush &amp; Toothpaste</span><span>2</span></li><li><span>Hair Brush</span><span>1</span></li><li><span>Hair Ties &amp; Headbands</span><span>3</span></li><li><span>Hair Spray</span><span>2</span></li><li><span>Glasses &amp; Contacts</span><span>5</span></li><li><span>MakeUp</span><span>5</span></li><li><span>Blow dryer or Flat Iron</span><span>1</span></li><li><span>Perfume</span><span>1</span></li><li><span>Feminine Products</span><span>1</span></li><li><span>Prescriptions</span><span>2</span></li><li><span>Vitamins</span><span>1</span></li><li><span>Sunblock</span><span>2</span></li></ul></div>
  <div class="abs pack" style="left:104px;top:62px;width:74px"><h5><span>CLOTHING</span><span>QTY.</span></h5>
    <ul class="dot"><li><span>Long Sleeve Shirts</span><span>2</span></li><li><span>Short Sleeve Shirts</span><span>2</span></li><li><span>Tanks</span><span>1</span></li><li><span>Shorts &amp; Skirts</span><span>6</span></li><li><span>Pants</span><span>8</span></li><li><span>Dresses</span><span>3</span></li><li><span>Pajamas</span><span>2</span></li><li><span>Shoes</span><span>2</span></li><li><span>Belts</span><span>1</span></li><li><span>Underwear &amp; Bras</span><span>3</span></li><li><span>Socks &amp; Tights</span><span>2</span></li><li><span>Swimsuit &amp; Cover Up</span><span>5</span></li><li><span>Jewelry</span><span>5</span></li><li><span>Sunglasses</span><span>2</span></li><li><span>Hat</span><span>1</span></li><li><span>Umbrella</span><span>1</span></li></ul></div>
  <div class="abs pack" style="left:190px;top:62px;width:78px"><h5><span>PAPER</span><span>QTY.</span></h5>
    <ul class="dot"><li><span>Tickets</span><span></span></li><li><span>License or Passport</span><span></span></li><li><span>Cash or Traveler's Checks</span><span></span></li><li><span>Copies of Reservations</span><span></span></li><li><span>Emergency Contact Info</span><span></span></li></ul>
    <h5 style="margin-top:4px"><span>ENTERTAINMENT</span><span></span></h5>
    <ul class="dot"><li><span>Phone + Charger</span><span>2</span></li><li><span>Laptop + Charger</span><span>1</span></li><li><span>Camera + Charger</span><span>1</span></li><li><span>Music Player</span><span>3</span></li><li><span>Outlet Converter</span><span>1</span></li><li><span>Books</span><span>5</span></li><li><span>eReader</span><span>1</span></li><li><span>Journal &amp; Pen</span><span>3</span></li><li><span>Guidebook</span><span>1</span></li></ul></div>
  <div class="abs pack" style="left:20px;top:212px;width:260px"><h5><span>KIDS</span><span></span></h5>
    <div style="display:grid;grid-template-columns:repeat(6,1fr);column-gap:4px">
      <ul class="dot"><li>Shirt</li><li>Shorts</li><li>Pants</li></ul>
      <ul class="dot"><li>Toothbrush</li><li>Toothpaste</li><li>Shampoo</li></ul>
      <ul class="dot"><li>Underwear</li><li>Socks</li><li>Shoes</li></ul>
      <ul class="dot"><li>Stuffed Animal</li><li>Blanket</li><li>Pillow</li></ul>
      <ul class="dot"><li>Coat</li><li>Sweatshirt</li></ul>
      <ul class="dot"><li>Pajamas</li><li>Swimsuit</li></ul>
    </div></div>
  <div class="photo" role="img" aria-label="Traveler packing a suitcase on a bed" style="left:22px;top:246px;width:256px;height:110px;background:linear-gradient(135deg,#e7e4df,#b8b2aa 50%,#3e3f48 80%,#d06a4a)"></div>
  <footer class="foot"><div class="brand"><b></b>Solavanti</div><div class="contact"><span>(USA) 1-800-555-0142</span><span>(ISRAEL) 972-50-555-0187</span><span>info@solavanti-travel.com</span><span>www.solavanti-travel.com</span></div><div class="pn">09</div></footer>
</div>

<!-- Back page -->
<div class="page" style="left:447px;top:1849px">
  <svg class="abs" style="left:0;top:0" width="300" height="250" viewBox="0 0 300 250">
    <defs><linearGradient id="backPhoto" x1="0" y1="0" x2="1" y2="1"><stop offset="0" stop-color="#b7a38c"/><stop offset=".5" stop-color="#7b5f4a"/><stop offset="1" stop-color="#c9b7a2"/></linearGradient></defs>
    <path role="img" aria-label="Family relaxing together on a sofa" d="M10 150 C0 80 40 20 110 14 C180 8 240 10 300 30 L300 236 C240 248 170 230 120 230 C60 230 18 210 10 150 Z" fill="url(#backPhoto)"/>
  </svg>
  <div class="brand" style="left:78px;top:310px;font-size:22px;gap:5px"><b style="width:16px;height:16px"></b>Solavanti</div>
  <div class="abs addr" style="left:80px;top:352px;font-size:4px">info@solavanti-travel.com &nbsp;&nbsp; www.solavanti-travel.com</div>
  <div class="abs" style="left:0;right:0;top:364px;height:1px;background:var(--orange)"></div>
  <div class="abs addr" style="left:42px;top:370px;width:120px"><b>USA</b><br>MN OFFICE - 210 Lakeview Court, Maple Bay, MN 55000<br>NY OFFICE - 88 Harbor Lane Suite 4B, New York, NY 10000<br><b>1-800-555-0142</b></div>
  <div class="abs addr" style="left:180px;top:370px;width:90px"><b>ISRAEL</b><br>Olive Row 12, Ein Tamar, Israel 3800000<br><b>972-50-555-0187</b></div>
</div>

</body>
</html>
```